Licensed Fabrication Operator Training Program

We need a flyer to advertise a training program to business. I will attach a rough draft "original file" that we need enhanced to look professional. Details to the program are here https://www.vornelskills.org/credentials/fabrication-credential-lfo/ We want it to look clean and professional.

Please use the information that is on the "original file" rough draft. I have attached an example pdf, the reason I don't like the example is because it has too many words and looks out of date.

Font styles to use
Serif
Sans Serif

```html
<!DOCTYPE html>
<html lang="en">
<head>
<meta charset="utf-8">
<title>Licensed Fabrication Operator Training Program</title>
<link href="https://fonts.googleapis.com/css2?family=Open+Sans:ital,wght@0,400;0,600;0,700;1,700;1,800&display=swap" rel="stylesheet">
<style>
  :root {
    --yellow: #fcc72a;
    --red: #e5403a;
    --ink: #2b2b2b;
    --green-ring: #8cc56f;
    --white: #ffffff;
    --muted: #444444;
  }
  html, body { margin: 0; padding: 0; overflow: hidden; }
  body { width: 929px; height: 1200px; background: var(--white); font-family: "Open Sans", Arial, sans-serif; }
  .flyer { position: relative; width: 929px; height: 1200px; overflow: hidden; background: var(--white); }

  .software-screens {
    position: absolute; left: 8px; top: 12px; width: 340px; height: 398px;
    background: linear-gradient(160deg, #f2f2f2 0%, #3f6fd0 45%, #b8c4d8 75%, #f4f4f4 100%);
  }
  .students-photo {
    position: absolute; left: 350px; top: 0; width: 579px; height: 380px;
    background: linear-gradient(100deg, #d9c3a9 0%, #b58d6a 30%, #e6d3b0 55%, #9fcf9a 80%, #dfe9d9 100%);
  }
  .brush-band { position: absolute; left: 0; top: 0; width: 929px; height: 900px; }

  .skills {
    position: absolute; left: 20px; top: 440px; width: 680px;
    transform: rotate(-3.5deg); transform-origin: left top;
  }
  .skills-title {
    margin: 0 0 8px 118px; font-weight: 800; font-style: italic;
    font-size: 62px; line-height: 1; color: var(--red);
  }
  .skills-columns { display: flex; position: relative; }
  .skills-columns::after {
    content: ""; position: absolute; left: 323px; top: 2px; bottom: 2px;
    width: 2px; background: var(--white);
  }
  .skills-list { list-style: none; margin: 0; padding: 0; }
  .skills-list li {
    font-weight: 700; font-style: italic; font-size: 31px; line-height: 41px;
    color: var(--ink); white-space: nowrap;
  }
  .skills-list.left { width: 318px; text-align: right; }
  .skills-list.right { padding-left: 16px; }

  .stat {
    position: absolute; width: 142px; height: 142px; border-radius: 50%;
    background: var(--white); border: 9px solid var(--green-ring);
    display: flex; flex-direction: column; align-items: center; justify-content: center;
    color: var(--ink); font-style: italic; text-align: center;
  }
  .stat-hours { left: 749px; top: 318px; }
  .stat-price { left: 633px; top: 438px; }
  .stat-reimb { left: 749px; top: 558px; }
  .stat .big { font-weight: 800; font-size: 58px; line-height: 0.9; }
  .stat .price { font-weight: 800; font-size: 36px; line-height: 1; }
  .stat .price sup { font-size: 20px; vertical-align: 10px; }
  .stat .label { font-weight: 700; font-size: 24px; line-height: 1.1; }
  .stat .label-sm { font-weight: 700; font-size: 18px; line-height: 1.1; }
  .stat .label-xs { font-weight: 700; font-size: 15px; line-height: 1.2; }

  .testimonial {
    position: absolute; left: 32px; top: 840px; width: 860px;
    transform: rotate(-3deg); transform-origin: left top; margin: 0; color: var(--ink);
  }
  .testimonial blockquote { margin: 0; font-size: 17px; line-height: 1.45; text-align: justify; }
  .testimonial figcaption { margin: 6px 0 0 660px; }
  .testimonial .name { display: block; font-weight: 700; font-size: 17px; }
  .testimonial .role { display: block; font-size: 11px; line-height: 1.4; margin-top: 6px; color: var(--muted); }

  .partners {
    position: absolute; left: 0; top: 970px; width: 929px; height: 197px; background: var(--yellow);
    display: flex; align-items: center; justify-content: space-around; padding: 0 30px; box-sizing: border-box;
  }
  .partner { display: flex; align-items: center; gap: 8px; font-weight: 700; font-size: 18px; color: var(--ink); }
  .partner .dot { width: 14px; height: 14px; border-radius: 50%; background: var(--ink); }
  .cert-badge { width: 70px; height: 108px; background: var(--white); border: 2px solid #1f6b3a; box-sizing: border-box; }
</style>
</head>
<body>
<main class="flyer">
  <div class="software-screens" role="img" aria-label="Collage of training software screens showing a caliper, gas cylinders, a pneumatic circuit and a multimeter lesson"></div>
  <div class="students-photo" role="img" aria-label="Photo of five smiling young students standing in a row holding notebooks"></div>

  <svg class="brush-band" viewBox="0 0 929 900" aria-hidden="true">
    <path fill="var(--yellow)" d="M0 470 L60 462 L120 458 L180 440 L260 432 L340 410 L380 402 L470 384 L520 378 L600 358 L660 352 L740 330 L820 312 L880 300 L929 268 L929 680 L890 692 L840 700 L780 712 L700 722 L620 740 L560 746 L480 766 L420 770 L340 786 L260 790 L200 800 L140 806 L80 808 L30 812 L0 806 Z"/>
    <path fill="var(--yellow)" d="M340 392 L400 370 L450 362 L470 374 Z M900 298 L929 280 L929 300 Z M20 806 L110 820 L60 812 Z"/>
  </svg>

  <section class="skills">
    <h2 class="skills-title">Skills Taught</h2>
    <div class="skills-columns">
      <ul class="skills-list left">
        <li>Communication</li><li>Lean Principles</li><li>Problem Solving</li><li>Teamwork</li><li>Locating Information</li>
      </ul>
      <ul class="skills-list right">
        <li>Communication</li><li>Lean Principles</li><li>Problem Solving</li><li>Teamwork</li><li>Locating Information</li>
      </ul>
    </div>
  </section>

  <div class="stat stat-hours"><span class="big">120</span><span class="label">Hours</span></div>
  <div class="stat stat-price"><span class="price"><sup>$</sup>2,500</span><span class="label-sm">Per Student</span></div>
  <div class="stat stat-reimb"><span class="big">WTP</span><span class="label-xs">Reimbursment</span></div>

  <figure class="testimonial">
    <blockquote>&ldquo;We feel that Vornel LFO certification compliments not only the qualifications of the candidates we see, but also enhance the knowledge, skills and abilities of existing team members in our pursuit of manufacturing excellence.&rdquo;</blockquote>
    <figcaption>
      <span class="name">Daniel Ferrow</span>
      <span class="role">Vice President &amp; General Manager<br>Corvane Drive Systems</span>
    </figcaption>
  </figure>

  <footer class="partners">
    <div class="partner"><span class="dot"></span>Northbay Standards</div>
    <div class="partner">Vornel</div>
    <div class="partner">Kestra</div>
    <div class="partner">Halden Motors</div>
    <div class="cert-badge" role="img" aria-label="Accreditation badge"></div>
  </footer>
</main>
</body>
</html>
```